Book Cover for Christian Book titled, "Climbing Past the Silver Hills"

Size of book cover will be 6" x 9".
The book is about how a person can know beyond a shadow of a doubt that they will go to heaven when they die.
The Title is "Climbing Past the Silver Hills"
Subtitle is "Finding Lasting Peace Through Daily Quiet Prayer and Reflection."
The front of the book should have title, subtitle, and author. The back of the book and spine should have no text and be a solid color.
The uploaded pic is a possibility for a design; but I'm open to other designs.
Whatever images are used need to be very high quality to meet Marrowind Folio Services guidelines. Also, the finished product needs to be sized to match the MFS guide for a 6x9 book.

```html
<!DOCTYPE html>
<html lang="en">
<head>
<meta charset="utf-8">
<title>Climbing Past the Silver Hills – Cover Layout</title>
<link rel="stylesheet" href="https://fonts.googleapis.com/css2?family=Bebas+Neue&family=Oswald:wght@200&family=Poppins:wght@300;600&display=swap">
<style>
  :root {
    --page-bg: #ffffff;
    --cover-blue: #0e5fad;
    --sky-top: #0f74cc;
    --sky-mid: #1aa0cf;
    --glow-yellow: #e8d232;
    --horizon-navy: #24406e;
    --deep-navy: #1c3458;
    --gold: #d4962a;
    --gold-line: #e69a1c;
    --band-olive: rgba(90, 70, 20, 0.78);
    --text-white: #ffffff;
    --panel-shadow: rgba(0, 0, 0, 0.38);
  }

  * { margin: 0; padding: 0; box-sizing: border-box; }

  html, body {
    width: 1200px;
    height: 806px;
    overflow: hidden;
    background: var(--page-bg);
  }

  .cover-spread {
    position: relative;
    width: 1200px;
    height: 806px;
  }

  .panel {
    position: absolute;
    top: 42px;
    height: 717px;
    box-shadow: 0 0 40px 6px var(--panel-shadow);
  }

  .panel--front { left: 45px; width: 479px; overflow: hidden; }
  .panel--spine { left: 560px; width: 76px; background: var(--cover-blue); }
  .panel--back  { left: 673px; width: 479px; background: var(--cover-blue); }

  .front-art {
    position: absolute;
    inset: 0;
    background:
      radial-gradient(ellipse 55% 35% at 62% 58%, rgba(240, 225, 70, 0.95), rgba(240, 225, 70, 0) 70%),
      radial-gradient(ellipse 40% 30% at 95% 45%, rgba(40, 60, 80, 0.55), rgba(40, 60, 80, 0) 70%),
      linear-gradient(180deg,
        var(--sky-top) 0%,
        var(--sky-mid) 35%,
        #5cb0c8 55%,
        #7d8a90 72%,
        var(--horizon-navy) 85%,
        var(--deep-navy) 100%);
  }

  .title-kicker-band {
    position: absolute;
    left: 58px;
    top: 78px;
    width: 340px;
    height: 61px;
    background: linear-gradient(90deg, var(--gold) 0%, rgba(212, 150, 42, 0.55) 55%, rgba(212, 150, 42, 0) 100%);
  }

  .title-kicker {
    position: absolute;
    left: 78px;
    top: 85px;
    font-family: "Oswald", sans-serif;
    font-weight: 200;
    font-size: 34px;
    line-height: 46px;
    letter-spacing: 2px;
    color: var(--text-white);
    white-space: nowrap;
  }

  .title-main {
    position: absolute;
    left: 55px;
    top: 180px;
    font-family: "Bebas Neue", sans-serif;
    font-size: 118px;
    line-height: 94px;
    letter-spacing: 9px;
    color: var(--text-white);
  }

  .subtitle-band {
    position: absolute;
    left: 30px;
    top: 474px;
    width: 449px;
    height: 100px;
    background: linear-gradient(90deg, var(--band-olive) 0%, rgba(110, 90, 30, 0.6) 60%, rgba(110, 90, 30, 0.1) 100%);
  }

  .subtitle {
    position: absolute;
    left: 56px;
    top: 497px;
    width: 395px;
    font-family: "Poppins", sans-serif;
    font-weight: 300;
    font-size: 19.5px;
    line-height: 27px;
    color: var(--text-white);
  }

  .subtitle strong { font-weight: 600; }

  .author-line {
    position: absolute;
    left: 77px;
    top: 652px;
    width: 316px;
    display: flex;
    align-items: center;
    justify-content: space-between;
  }

  .author-rule {
    width: 40px;
    height: 2px;
    background: var(--gold-line);
  }

  .author-name {
    font-family: "Poppins", sans-serif;
    font-weight: 300;
    font-size: 31px;
    line-height: 40px;
    color: var(--text-white);
  }
</style>
</head>
<body>
  <main class="cover-spread">
    <section class="panel panel--front">
      <div class="front-art" role="img" aria-label="Sunlit sky with rays breaking through clouds above a glowing cross and an open book"></div>

      <div class="title-kicker-band"></div>
      <p class="title-kicker">CLIMBING PAST THE</p>
      <h1 class="title-main">SILVER<br>HILLS</h1>

      <div class="subtitle-band"></div>
      <p class="subtitle">Finding Lasting Peace Through <strong>Daily Quiet Prayer and Reflection.</strong></p>

      <div class="author-line">
        <span class="author-rule"></span>
        <span class="author-name">Author Name</span>
        <span class="author-rule"></span>
      </div>
    </section>

    <section class="panel panel--spine" aria-label="Spine"></section>
    <section class="panel panel--back" aria-label="Back cover"></section>
  </main>
</body>
</html>
```